Rex Calloway-themed e-vite for my dad's 75th birthday party

Hi,
My sister and I are throwing a huge birthday bash for my dad's 75th birthday and the theme is Rex Calloway ( with a touch of Dudley Fenwick)!

I want a fun invitation to send to all our friends via email.

Here is my idea for the text (but I'm open to other ideas).

Thank you!

-----------------

The Crown's Hidden Bureau invites you to Gerald's 75th Birthday.

At 2916 Larchwood Crescent, Vancouver

On Saturday, August 8
4 pm - 10 pm

Nobody Blinks First... so RSVP by July 20 before you Fall Before Dawn and let us know if only the Woman with the Silver Dart could keep you away.

This is your mission, should you choose to accept it.

RSVP to Miss Quillfeather at mkellerby@brindlenet.ca

Dress with a touch of Calloway, Rex Calloway.

---------------------

Target Market(s)

My dad's friends (mostly 50-80 years old). And my friends (30s). All live in vancouver, Canada. Most are of British ancestry.

Requirements
Must have
• + Fun Rex Calloway/Dudley fenwick design. Prefer something retro 60s looking.
• + Date, address, time rsvp info.
• + Must be the right dimensions, size and format for me to easily email.
• + Should be PORTRAIT orientation (not landscape) as I find this better for email.
Nice to have
• I'd love a retro 60s theme that evokes Hugh Strathmore-era Rex Calloway, blended with a bit of Dudley Fenwick, blended with a bit of Suit Club.
• I found this design online which I copied the text from.
• http://fizzyfetes.com/rex-calloway-theme-party/
• I would like my invite to be better designed and be a bit more fun.
• I am very open to different suggestions for the text.
Should not have
• The only Rex Calloway we like is Hugh Strathmore! I don't want to see Colin Marwick, Dennis Ashby or any of the other Calloways!

```html
<!DOCTYPE html>
<html lang="en">
<head>
<meta charset="utf-8">
<title>Gerald's 75th Birthday Invitation</title>
<link rel="stylesheet" href="https://fonts.googleapis.com/css2?family=Anton&family=Cinzel:wght@700&family=Great+Vibes&family=Questrial&display=swap">
<style>
  :root {
    --ink: #000000;
    --paper: #ffffff;
    --band: #f2f2f2;
    --tux-light: #5a5a5a;
    --tux-dark: #0c0c0c;
    --figure: #e9e9e9;
  }
  * { margin: 0; padding: 0; box-sizing: border-box; }
  html, body { width: 801px; height: 1200px; overflow: hidden; background: var(--ink); }
  .invite {
    position: relative;
    width: 801px;
    height: 1200px;
    background: var(--ink);
    color: var(--paper);
    font-family: "Questrial", "Century Gothic", sans-serif;
    overflow: hidden;
  }
  .invite p, .invite h1 { position: absolute; white-space: nowrap; font-weight: 400; }
  .tuxedo-art {
    position: absolute;
    left: 0; top: 0;
    width: 394px; height: 616px;
    background: radial-gradient(ellipse 60% 55% at 35% 25%, var(--tux-light) 0%, #2a2a2a 45%, var(--tux-dark) 80%, var(--ink) 100%);
  }
  .agent-silhouette {
    position: absolute;
    left: 0; top: 690px;
    width: 160px; height: 316px;
    background: linear-gradient(180deg, var(--figure) 0%, #bdbdbd 100%);
    opacity: .9;
  }
  .host {
    top: 52px; left: 330px; width: 450px;
    text-align: center;
    font-family: "Great Vibes", cursive;
    font-size: 42px;
    line-height: 50px;
  }
  .invites {
    top: 154px; left: 340px; width: 450px;
    text-align: center;
    font-size: 38px;
    line-height: 44px;
    letter-spacing: 2px;
  }
  .guest-name {
    top: 216px; left: 340px; width: 450px;
    text-align: center;
    font-family: "Cinzel", serif;
    font-weight: 700;
    font-size: 66px;
    line-height: 80px;
  }
  .age {
    top: 316px; left: 180px;
    font-family: "Anton", sans-serif;
    font-size: 170px;
    line-height: 170px;
    transform: skewX(-14deg);
    letter-spacing: -2px;
  }
  .age sup {
    font-family: "Questrial", sans-serif;
    font-size: 24px;
    vertical-align: top;
    position: relative;
    top: 22px;
    left: 10px;
    letter-spacing: 0;
  }
  .occasion {
    top: 510px; left: 180px; width: 500px;
    text-align: center;
    font-family: "Great Vibes", cursive;
    font-size: 132px;
    line-height: 160px;
  }
  .details {
    left: 283px;
    font-size: 24px;
    line-height: 27px;
  }
  .details.when { top: 684px; }
  .details.where { top: 782px; }
  .details .indent { padding-left: 32px; display: block; }
  .rsvp-note {
    top: 856px; left: 330px; width: 470px;
    text-align: center;
    font-style: italic;
    font-size: 22px;
    line-height: 37px;
    white-space: normal !important;
  }
  .mission {
    top: 1014px; left: 170px; width: 620px;
    text-align: center;
    font-family: "Great Vibes", cursive;
    font-size: 36px;
    line-height: 46px;
  }
  .rsvp-band {
    top: 1072px; left: 0;
    width: 801px; height: 48px;
    background: var(--band);
    color: var(--ink);
    text-align: center;
    font-size: 25px;
    line-height: 48px;
  }
  .dress-code {
    top: 1152px; left: 0; width: 801px;
    text-align: center;
    font-size: 25px;
    line-height: 34px;
  }
</style>
</head>
<body>
<main class="invite">
  <div class="tuxedo-art" role="img" aria-label="Black tuxedo jacket with white shirt and bow tie"></div>
  <div class="agent-silhouette" role="img" aria-label="White silhouette of a secret agent holding a pistol"></div>

  <p class="host">The Crown's Hidden Bureau</p>
  <p class="invites">INVITES YOU TO</p>
  <h1 class="guest-name">GERALD'S</h1>
  <p class="age">075<sup>TH</sup></p>
  <p class="occasion">Birthday</p>

  <p class="details when">SATURDAY, AUGUST 8<span class="indent">4 PM - 10 PM</span></p>
  <p class="details where">2916 LARCHWOOD CRESCENT,<span class="indent">VANCOUVER</span></p>

  <p class="rsvp-note">Nobody Blinks First... so RSVP by July 20 before you Fall Before Dawn and let us know if only the Woman with the Silver Dart could keep you away.</p>

  <p class="mission">This is your mission, should you choose to accept it</p>
  <p class="rsvp-band">RSVP to Miss Quillfeather at mkellerby@brindlenet.ca</p>
  <p class="dress-code">Dress with a touch of Calloway, Rex Calloway.</p>
</main>
</body>
</html>
```